Saffron Lotus Court Business Card

I am looking for a business card desgined for my restaurant. It is an Indian restaurant, we are looking for something thats modern, yet traditional with the indian culture, we are looking for colors that match our logo. The logo is a design of the building with the name of the restaurant. for more information on the restaurant go to www.saffronlotuscourt.example

Industry/Entity Type

Indian Restaurant

Contact Information for Business Card

we are looking for somthing thats modern, yet traditional with the indian culture, we are looking for colors that match our logo. The logo is a design of the building with the name of the restaurant. for more information on the restaurant go to www.saffronlotuscourt.example

Requirements
Must have
• The logo that is attached,
• Name: Harjot Banwal,
• address of the restaurant: 2917 West Tamarind Ave, Phoenix, Arizona, 85047
• Phone: (602) 517-3094
• Fax: (602) 768-2145
• Restaurant Catering Banquet
• Website: www.SaffronLotusCourt.example
Nice to have
• wanted to get something that goes with the theme of the restaurant, which is traditional but also keep a very professional and modern touch

```html
<!DOCTYPE html>
<html lang="en">
<head>
<meta charset="utf-8">
<title>Saffron Lotus Court Business Card</title>
<link href="https://fonts.googleapis.com/css2?family=Lato:wght@400;700&display=swap" rel="stylesheet">
<style>
  :root {
    --backdrop: #4a4a4a;
    --card-dark: #262525;
    --card-light: #ffffff;
    --saffron: #f26a21;
    --chili: #c0272d;
    --ink: #5a5a5a;
    --pattern-dark: #2b2a2a;
    --pattern-light: #f7f7f7;
  }
  * { box-sizing: border-box; margin: 0; padding: 0; }
  html, body {
    width: 1200px; height: 1000px; overflow: hidden;
    background: var(--backdrop);
    font-family: "Lato", sans-serif;
  }
  .canvas { position: relative; width: 1200px; height: 1000px; }
  .card {
    position: absolute; top: 106px; width: 449px; height: 787px; overflow: hidden;
  }
  .card--front { left: 135px; background: var(--card-dark); }
  .card--back { left: 616px; background: var(--card-light); }
  .card__pattern { position: absolute; inset: 0; }
  .card--front .card__pattern { background: radial-gradient(circle at 60% 30%, var(--pattern-dark), var(--card-dark) 70%); }
  .card--back .card__pattern { background: radial-gradient(circle at 60% 40%, var(--pattern-light), var(--card-light) 70%); }
  .brand {
    position: absolute; left: 0; right: 0; text-align: center;
  }
  .card--front .brand { top: 380px; }
  .card--back .brand { top: 240px; }
  .brand__name {
    font-family: "Lato", sans-serif; font-weight: 700;
    color: var(--saffron); font-size: 52px; line-height: 1.22;
    text-transform: uppercase; letter-spacing: 3px;
  }
  .brand__since {
    margin-top: 22px; color: var(--chili);
    font-size: 13px; font-weight: 700; letter-spacing: 3px;
  }
  .contact { position: absolute; left: 102px; top: 520px; color: var(--ink); }
  .contact__name { color: var(--saffron); font-size: 22px; font-weight: 700; line-height: 1.2; }
  .contact__role { font-size: 16px; margin-top: 2px; }
  .contact__address { font-size: 16px; line-height: 22px; margin-top: 16px; }
  .contact__list { list-style: none; margin-top: 14px; font-size: 16px; }
  .contact__list li { display: flex; align-items: center; height: 25.5px; }
  .contact__icon { width: 13px; height: 13px; margin-right: 11px; fill: var(--chili); }
</style>
</head>
<body>
<main class="canvas">
  <section class="card card--front">
    <div class="card__pattern" role="img" aria-label="Faint paisley pattern in dark charcoal tones"></div>
    <div class="brand">
      <div class="brand__name">Saffron<br>Lotus<br>Court</div>
      <div class="brand__since">SINCE 1985</div>
    </div>
  </section>

  <section class="card card--back">
    <div class="card__pattern" role="img" aria-label="Faint paisley pattern in light grey tones"></div>
    <div class="brand">
      <div class="brand__name">Saffron<br>Lotus<br>Court</div>
      <div class="brand__since">SINCE 1985</div>
    </div>
    <div class="contact">
      <div class="contact__name">Harjot Banwal</div>
      <div class="contact__role">Founder &amp; CEO</div>
      <div class="contact__address">2917 West Tamarind Ave,<br>Phoenix, Arizona, 85047</div>
      <ul class="contact__list">
        <li>
          <svg class="contact__icon" viewBox="0 0 16 16" aria-hidden="true"><path d="M3.5 1l3 3-1.8 1.8c.9 2 2.5 3.6 4.5 4.5L11 8.5l3 3-2 2.5C6.5 13.5 2.5 9.5 1 4z"/></svg>
          (602) 517-3094
        </li>
        <li>
          <svg class="contact__icon" viewBox="0 0 16 16" aria-hidden="true"><path d="M4 1h8v4H4zM1 6h14v6h-3v3H4v-3H1zm4 4v4h6v-4z"/></svg>
          (602) 768-2145
        </li>
        <li>
          <svg class="contact__icon" viewBox="0 0 16 16" aria-hidden="true"><path d="M8 1a7 7 0 100 14A7 7 0 008 1zm0 1.5c.8 0 1.7 1.6 2 4H6c.3-2.4 1.2-4 2-4zM2.6 7h2.4c0 .7 0 1.3.1 2H2.6a5.5 5.5 0 010-2zm8.4 0h2.4a5.5 5.5 0 010 2H11c.1-.7.1-1.3 0-2zM6.1 9.5h3.8c-.3 2.4-1.2 4-1.9 4s-1.6-1.6-1.9-4z"/></svg>
          www.SaffronLotusCourt.example
        </li>
      </ul>
    </div>
  </section>
</main>
</body>
</html>
```